Event Planner Looking To Set Apart From Competition

I am a experienced Event/Wedding planner and need to design a unique marketing piece that will be handed out to clients and venues. I would like a postcard, but I am not opposed to another style of printed piece if it's cost effective. I am also looking for a logo that is unique to me and would like to see a few ideas.

Target Market(s)

Brides and Social Event Organizers

Industry/Entity Type

Wedding Planner

Logo Text

Mara Thistlewood

Font styles to use
Script

Colors
ffffff
fee3d4
fff3d1
cfeae6
cee9f5
ecdaeb
cedeed

Requirements
Must have
• website reference _ http://www.qrvgatherings.example/planning-packages
• blog reference _ https://blogqrvgatherings.example/meet-mara/
Nice to have
• We can add text once a layout is proposed. If we like the general layout, we will send the text to be included based on the layout.

```html
<!DOCTYPE html>
<html lang="en">
<head>
<meta charset="utf-8">
<title>Mara Thistlewood – Wedding Planning Postcard</title>
<link rel="stylesheet" href="https://fonts.googleapis.com/css2?family=Aladin&family=Lato:wght@400&family=Lobster+Two:ital,wght@1,700&family=Marcellus+SC&family=Montserrat:wght@400&display=swap">
<style>
  :root {
    --stage: #e6e6e6;
    --blush: #fee3d4;
    --sky: #9fdcf5;
    --band-light: #ffffff;
    --band-grey: #dcdcdc;
    --magenta: #b0168f;
    --plum: #6e1550;
    --ink: #2f2f2f;
    --slate: #555a5e;
    --photo-warm: #8a7a64;
    --photo-green: #4f6b3a;
    --mark-dark: #1c1c1c;
  }
  * { margin: 0; padding: 0; box-sizing: border-box; }
  html, body {
    width: 1200px; height: 1200px; overflow: hidden;
    background: var(--stage);
  }
  .postcard {
    position: absolute; left: 40px; top: 200px;
    width: 1120px; height: 800px;
    background: var(--blush);
    box-shadow: 0 6px 20px rgba(0,0,0,.18);
    overflow: hidden;
  }
  .postcard__art { position: absolute; inset: 0; }
  .brand {
    position: absolute; left: 670px; top: 384px; width: 420px;
    text-align: center; color: var(--slate);
    font-family: "Montserrat", sans-serif; font-weight: 400;
  }
  .brand__name { font-size: 31px; letter-spacing: 1px; line-height: 1; white-space: nowrap; }
  .brand__tagline { font-size: 11px; letter-spacing: 3px; margin-top: 7px; }
  .headline {
    position: absolute; right: 46px; top: 442px;
    font-family: "Aladin", cursive; font-weight: 400; color: var(--magenta);
    font-size: 90px; line-height: 1; white-space: nowrap;
  }
  .subline {
    position: absolute; right: 60px; top: 538px;
    font-family: "Aladin", cursive; color: var(--ink);
    font-size: 41px; line-height: 47px; text-align: right; white-space: nowrap;
  }
  .packages {
    position: absolute; left: 51px; top: 602px;
  }
  .packages__title {
    font-family: "Marcellus SC", serif; font-weight: 400; color: var(--plum);
    font-size: 31px; line-height: 1; margin-bottom: 16px; white-space: nowrap;
  }
  .packages__list { list-style: none; }
  .packages__item {
    font-family: "Lobster Two", cursive; font-style: italic; font-weight: 700;
    color: var(--ink); font-size: 25px; line-height: 35px; white-space: nowrap;
  }
  .contact {
    position: absolute; left: 628px; top: 686px;
    list-style: none; font-family: "Lato", sans-serif;
    color: var(--ink); font-size: 15.5px;
  }
  .contact__row { display: flex; align-items: center; gap: 9px; height: 21px; white-space: nowrap; }
  .contact__icon { width: 14px; height: 14px; flex: none; }
  .contact__row--small { font-size: 14px; }
</style>
</head>
<body>
<main class="postcard">
  <svg class="postcard__art" viewBox="0 0 1120 800" width="1120" height="800">
    <defs>
      <linearGradient id="couplePhoto" x1="0" y1="0" x2="1" y2="1">
        <stop offset="0" stop-color="#f1ece6"/>
        <stop offset=".45" stop-color="var(--photo-warm)"/>
        <stop offset="1" stop-color="#5b4e3e"/>
      </linearGradient>
      <linearGradient id="venuePhoto" x1="0" y1="0" x2="0" y2="1">
        <stop offset="0" stop-color="#c9cfc3"/>
        <stop offset=".35" stop-color="var(--photo-green)"/>
        <stop offset="1" stop-color="#6b4a3c"/>
      </linearGradient>
      <linearGradient id="bandFade" x1="0" y1="0" x2="1" y2="0">
        <stop offset="0" stop-color="var(--band-light)"/>
        <stop offset=".45" stop-color="var(--band-light)"/>
        <stop offset="1" stop-color="var(--band-grey)"/>
      </linearGradient>
    </defs>

    <rect class="photo photo--couple" x="0" y="0" width="582" height="470" fill="url(#couplePhoto)"
          role="img" aria-label="Photo of a bride and groom cutting a tall white rose-covered wedding cake"/>
    <rect class="photo photo--venue" x="590" y="0" width="530" height="342" fill="url(#venuePhoto)"
          role="img" aria-label="Photo of a reception hall with a floral canopy, hanging crystals and candlelit tables"/>

    <path class="wave wave--blush" fill="var(--blush)"
          d="M0,412 C180,440 330,430 480,395 C560,376 600,350 660,342 L1120,342 L1120,800 L0,800 Z"/>

    <path class="wave wave--band" fill="url(#bandFade)"
          d="M0,448 C300,420 620,290 880,300 C1000,306 1080,340 1120,372 L1120,650 C1000,670 900,690 812,676 C650,650 480,580 300,540 C180,514 80,505 0,508 Z"
          role="img" aria-label="Faded photo of a wedding ceremony inside a chapel"/>

    <path class="wave-line" fill="none" stroke="var(--sky)" stroke-width="7"
          d="M0,448 C300,420 620,290 880,300 C1000,306 1080,340 1120,372"/>
    <path class="wave-line" fill="none" stroke="var(--sky)" stroke-width="7"
          d="M0,508 C80,505 180,514 300,540 C480,580 650,650 812,676 C900,690 1000,670 1120,650"/>

    <circle class="brand__mark" cx="876" cy="315" r="62" fill="var(--mark-dark)"/>
  </svg>

  <div class="brand">
    <div class="brand__name">MARA THISTLEWOOD</div>
    <div class="brand__tagline">THISTLEWOOD EVENT PRODUCTION</div>
  </div>

  <h1 class="headline">You’re engaged</h1>
  <p class="subline">and it’s time for the<br>wedding planning to begin</p>

  <section class="packages">
    <h2 class="packages__title">Wedding Planning Packages</h2>
    <ul class="packages__list">
      <li class="packages__item">Full Planning &amp; Coordination</li>
      <li class="packages__item">Partial Planning &amp; Coordination</li>
      <li class="packages__item">Month Of Planning &amp; Coordination</li>
    </ul>
  </section>

  <ul class="contact">
    <li class="contact__row">
      <svg class="contact__icon" viewBox="0 0 16 16"><circle cx="8" cy="8" r="7" fill="none" stroke="currentColor" stroke-width="1.4"/><path d="M5.3 4.3l1.4 1.6-.7 1c.5 1.1 1.3 1.9 2.4 2.4l1-.7 1.6 1.4-.9 1.3C7.5 11 5 8.5 4.4 5.2z" fill="currentColor"/></svg>
      <span>888.555.0142</span>
    </li>
    <li class="contact__row">
      <svg class="contact__icon" viewBox="0 0 16 16"><rect x="4" y="2" width="8" height="4" fill="currentColor"/><rect x="1" y="6" width="14" height="7" rx="1" fill="currentColor"/><rect x="4" y="10" width="8" height="2" fill="#fff"/></svg>
      <span>678.555.0199</span>
    </li>
    <li class="contact__row contact__row--small">
      <svg class="contact__icon" viewBox="0 0 16 16"><circle cx="8" cy="8" r="7" fill="none" stroke="currentColor" stroke-width="1.4"/><path d="M8 3.5a2.8 2.8 0 0 0-2.8 2.8C5.2 8.5 8 12 8 12s2.8-3.5 2.8-5.7A2.8 2.8 0 0 0 8 3.5zm0 3.9a1.1 1.1 0 1 1 0-2.2 1.1 1.1 0 0 1 0 2.2z" fill="currentColor"/></svg>
      <span>1420 Larkspur Commerce Way, Suite 210 Ashford Ga, 30000</span>
    </li>
    <li class="contact__row contact__row--small">
      <svg class="contact__icon" viewBox="0 0 16 16"><circle cx="8" cy="8" r="7" fill="none" stroke="currentColor" stroke-width="1.4"/><ellipse cx="8" cy="8" rx="3" ry="7" fill="none" stroke="currentColor" stroke-width="1.2"/><path d="M1 8h14" stroke="currentColor" stroke-width="1.2"/></svg>
      <span>www.qrvgatherings.example/planning-packages</span>
    </li>
    <li class="contact__row contact__row--small">
      <svg class="contact__icon" viewBox="0 0 16 16"><rect x="2" y="2" width="12" height="12" rx="1.5" fill="none" stroke="currentColor" stroke-width="1.4"/><path d="M5 6h6M5 8.5h6M5 11h4" stroke="currentColor" stroke-width="1.2"/></svg>
      <span>blogqrvgatherings.example/meet-mara/</span>
    </li>
  </ul>
</main>
</body>
</html>
```